Modern Homepage Design for brenvik.nl – Fish & Chicken Food Webshop

Brenvik.nl is an online store that sells fish and chicken food. The design should be visually appealing, easy to navigate, and optimized for e-commerce. We want a layout that helps customers quickly find what they need and encourages them to explore our products.
A good example of the style and structure we like is dierkamp.nl – clean layout, clear product focus, and user-friendly navigation.
Brand Colors (must be used):
Orange: #f7a441
Dark Gray: #3c3c3b
White: #ffffff
Please use these colors consistently throughout the design.
Homepage Requirements:
The homepage should include the following sections:
Main Slider / Hero Banner
A large, eye-catching slider at the top of the page to highlight promotions or featured categories.
Category Blocks
A section with clear, clickable blocks or tiles that link to main product categories (e.g., Fish Food, Chicken Food, Accessories).
Featured Products
A section showcasing selected or best-selling products.
Special Offers / Promotions
A space to highlight current deals or limited-time offers.
Three Banners in a Row
A section with three horizontal banners side by side, which can be used for promotions, shipping info, or other key messages.
Unique Selling Points (USPs)
A section that briefly explains what makes our store different (e.g., fast delivery, high-quality feed, trusted by professionals).
SEO Content Block
A short paragraph of text for SEO purposes (use Lorem Ipsum for dummy content).
Footer Design
Include space for contact information, navigation links, and social media.
Design Notes:
The design must be responsive and mobile-friendly.
Focus on clean layout, good spacing, and easy navigation.
Use modern fonts and a clear visual hierarchy.
We are only looking for the homepage design at this stage, but we may work with the selected designer on additional pages later.
Deliverables:
Homepage design in layered PSD, Figma, or Adobe XD format
Any fonts and assets used
Preview images/mockups
We look forward to seeing your ideas and working with a designer who can bring our brand to life with a fresh and functional homepage design.
Let us know if you have any questions.
Hobby Animal Keepers, Pet Owners
Animal Nutrition & Feed
2 page

```html
<!DOCTYPE html>
<html lang="en">
<head>
<meta charset="utf-8">
<title>Brenvik.nl – Fish & Poultry Feed</title>
<link rel="stylesheet" href="https://fonts.googleapis.com/css2?family=Red+Hat+Display:wght@400;500;600;700;800&display=swap">
<style>
:root{
  --orange:#f7a441;
  --orange-soft:#fde3c2;
  --dark:#3c3c3b;
  --white:#ffffff;
  --card:#f2f2f2;
  --text:#3c3c3b;
  --muted:#555;
  --line:#dcdcdc;
  --about-text:#ececec;
}
*{box-sizing:border-box;margin:0;padding:0}
html,body{width:1200px;height:3591px;overflow:hidden}
body{position:relative;background:var(--white);font-family:"Red Hat Display",sans-serif;color:var(--text)}
.abs{position:absolute}
.topbar{left:0;top:0;width:1200px;height:31px;background:var(--dark);color:var(--white);font-size:11px;font-weight:500}
.topbar span{position:absolute;top:9px;display:flex;align-items:center;gap:6px}
.topbar svg{width:11px;height:11px;fill:var(--orange)}
.brand{font-weight:700;color:var(--dark);display:flex;align-items:center;gap:8px}
.brand i{display:block;border-radius:50%;background:var(--orange)}
.nav{left:368px;top:76px;display:flex;gap:24px;font-size:10.5px;font-weight:500;letter-spacing:.1px}
.search{left:740px;top:61px;width:222px;height:41px;border-radius:21px;background:#eee;font-size:11px;color:#999;padding:13px 22px}
.search svg{position:absolute;right:18px;top:13px;width:14px;height:14px}
.iconbtn{width:34px;height:34px;border-radius:50%;border:1px solid #ddd;display:flex;align-items:center;justify-content:center}
.iconbtn svg{width:13px;height:13px;fill:var(--dark)}
.btn{display:flex;align-items:center;justify-content:space-between;background:var(--orange);color:var(--white);border-radius:24px;font-size:11px;font-weight:700;letter-spacing:.3px;padding:0 7px 0 42px}
.btn b{width:32px;height:32px;border-radius:50%;background:var(--white);display:flex;align-items:center;justify-content:center}
.btn b svg{width:14px;height:14px}
.hero{left:89px;top:134px;width:1019px;height:504px;border-radius:48px;background:linear-gradient(90deg,#fff5ea 0%,#fde6c8 45%,#f9b865 100%);overflow:hidden}
h1{font-size:34px;font-weight:700;line-height:1.0}
.lead{font-size:13px;line-height:18px;color:var(--muted)}
.ph{border-radius:20px}
h2{font-size:27px;font-weight:700}
.catcard{top:882px;width:329px;height:155px;border-radius:22px}
.cattitle{font-size:15px;font-weight:600;text-align:center;width:329px}
.catdesc{font-size:11.5px;text-align:center;width:329px;color:var(--muted)}
.prod{top:1280px;width:187px;height:283px;border-radius:18px;background:var(--card)}
.prod .img{position:absolute;left:58px;top:25px;width:70px;height:100px;border-radius:10px}
.stars{position:absolute;left:30px;top:150px;display:flex;gap:1px}
.stars svg{width:14px;height:14px}
.pname{position:absolute;left:30px;top:177px;font-size:12px;font-weight:500;line-height:15px;width:140px}
.price{position:absolute;left:30px;top:220px;font-size:18px;font-weight:700}
.price small{font-size:9px;font-weight:500;margin-left:4px}
.cart{position:absolute;left:140px;top:223px;width:16px;height:16px;fill:var(--orange)}
.usp{display:flex;gap:15px;align-items:center}
.usp .c{width:88px;height:88px;border-radius:50%;display:flex;align-items:center;justify-content:center}
.usp .c svg{width:40px;height:40px;fill:var(--white)}
.usp h4{font-size:15px;font-weight:600;margin-bottom:6px}
.usp p{font-size:13px;line-height:18px;color:var(--muted)}
.list{left:88px;top:2368px;width:345px;list-style:none}
.list li{height:41px;border-bottom:1px solid var(--line);display:flex;align-items:center;gap:10px;font-size:13px}
.list li:last-child{border-bottom:none}
.list svg{width:13px;height:13px}
.about{left:0;top:2768px;width:1200px;height:407px;background:linear-gradient(120deg,#4a4a49,#3c3c3b);border-radius:72px}
.about-copy{left:95px;top:2907px;width:470px}
.about-copy p{font-size:13px;line-height:20px;color:var(--about-text)}
.fcol h5{font-size:17px;font-weight:600;margin-bottom:12px}
.fcol a{display:block;font-size:11px;color:var(--text);text-decoration:none;line-height:24px}
.fcol .ci{display:flex;gap:8px}
.fcol .ci svg{width:11px;height:11px;fill:var(--orange);margin-top:6px;flex:none}
.social{width:40px;height:40px;border-radius:50%;background:#eee}
</style>
</head>
<body>

<div class="abs topbar">
  <span style="left:105px"><svg viewBox="0 0 24 24"><path d="M2 5h20v14H2z"/></svg>info@brenvik.nl</span>
  <span style="left:228px"><svg viewBox="0 0 24 24"><path d="M6 2l4 5-2 3c1 3 3 5 6 6l3-2 5 4-3 4C10 21 3 14 2 5z"/></svg>0612457830</span>
  <span style="left:412px">Free Shipping on Orders Over €49 | Fast Delivery Across the Netherlands</span>
  <span style="left:958px"><svg viewBox="0 0 24 24"><path d="M6 2l4 5-2 3c1 3 3 5 6 6l3-2 5 4-3 4C10 21 3 14 2 5z"/></svg>Questions? 085-3341208</span>
</div>

<div class="abs brand" style="left:91px;top:58px;font-size:40px"><i style="width:36px;height:36px"></i>brenvik</div>
<nav class="abs nav"><span>CATEGORIES</span><span>ABOUT US</span><span>BLOG</span><span>CONTACT</span><span>% OFFERS</span></nav>
<div class="abs search">Search our store...<svg viewBox="0 0 24 24" fill="none" stroke="#3c3c3b" stroke-width="2.5"><circle cx="10" cy="10" r="7"/><path d="M15 15l6 6"/></svg></div>
<div class="abs iconbtn" style="left:992px;top:64px"><svg viewBox="0 0 24 24"><circle cx="12" cy="7" r="5"/><path d="M3 22c0-6 4-9 9-9s9 3 9 9z"/></svg></div>
<div class="abs iconbtn" style="left:1034px;top:64px"><svg viewBox="0 0 24 24"><path d="M12 21L3 12a5 5 0 017-7l2 2 2-2a5 5 0 017 7z"/></svg></div>
<div class="abs iconbtn" style="left:1076px;top:64px"><svg viewBox="0 0 24 24"><path d="M2 3h4l3 11h11l3-8H7"/><circle cx="10" cy="19" r="2"/><circle cx="18" cy="19" r="2"/></svg></div>

<section class="abs hero">
  <div class="abs ph" role="img" aria-label="Red and orange betta fighter fish with 'the fighter fish' lettering" style="left:450px;top:120px;width:470px;height:330px;background:radial-gradient(ellipse at 55% 50%,#e0431c 0%,#f07a35 40%,rgba(247,164,65,0) 72%)"></div>
</section>
<h1 class="abs" style="left:176px;top:216px">Premium Feed for<br>Fish and Poultry</h1>
<p class="abs lead" style="left:178px;top:300px">Trusted by farms, breeders, and hobbyists for over<br>25 years. Shop high-quality feed and supplies.</p>
<div class="abs btn" style="left:173px;top:358px;width:173px;height:45px">SHOP NOW <b><svg viewBox="0 0 24 24" fill="none" stroke="#f7a441" stroke-width="3"><path d="M5 12h13M13 6l6 6-6 6"/></svg></b></div>
<div class="abs" role="img" aria-label="Rooster standing in a dotted circle" style="left:135px;top:460px;width:240px;height:272px;border-radius:50%;background:radial-gradient(ellipse,#c8612a 0%,#e79a4f 45%,rgba(255,255,255,0) 72%)"></div>
<div class="abs" role="img" aria-label="Bowl of poultry grain pellets" style="left:414px;top:596px;width:94px;height:94px;border-radius:50%;background:radial-gradient(circle,#c99a57,#8a6a3e)"></div>
<div class="abs" role="img" aria-label="Bowl of fine fish feed granules" style="left:524px;top:596px;width:94px;height:94px;border-radius:50%;background:radial-gradient(circle,#8c6a52,#4e3c33)"></div>

<h2 class="abs" style="left:87px;top:785px">Shop by Category</h2>
<div class="abs catcard" style="left:89px;background:#efefef"></div>
<div class="abs catcard" style="left:435px;background:var(--orange-soft)"></div>
<div class="abs catcard" style="left:779px;background:#efefef"></div>
<div class="abs ph" role="img" aria-label="Orange koi fish with a feed pack" style="left:170px;top:836px;width:210px;height:200px;background:radial-gradient(ellipse,#f08a2a,#f4b25f 50%,rgba(255,255,255,0) 72%)"></div>
<div class="abs ph" role="img" aria-label="Hen beside a chicken feed bag" style="left:495px;top:836px;width:210px;height:200px;background:radial-gradient(ellipse,#9a5226,#c77b45 50%,rgba(255,255,255,0) 72%)"></div>
<div class="abs ph" role="img" aria-label="Metal feed tray on orange stand" style="left:840px;top:852px;width:210px;height:185px;background:radial-gradient(ellipse,#9fa8b3,#b9c0c8 50%,rgba(255,255,255,0) 72%)"></div>
<div class="abs cattitle" style="left:89px;top:1058px">Fish Food</div>
<div class="abs catdesc" style="left:89px;top:1088px">Nutrient-rich feed for healthy and vibrant fish.</div>
<div class="abs cattitle" style="left:435px;top:1058px">Chicken Food</div>
<div class="abs catdesc" style="left:435px;top:1087px">Balanced nutrition for strong &amp; productive poultry.</div>
<div class="abs cattitle" style="left:779px;top:1058px">Acessories</div>
<div class="abs catdesc" style="left:779px;top:1087px">Supplements, and more essentials for your animals.</div>

<h2 class="abs" style="left:86px;top:1193px">Best Sellers</h2>
<p class="abs" style="left:88px;top:1231px;font-size:11.5px;color:var(--muted)">Our most popular products, loved by farms and hobbyists across the country.</p>

<svg width="0" height="0" style="position:absolute"><defs><path id="star" d="M12 2l3 7h7l-6 4 2 8-6-4-6 4 2-8-6-4h7z"/></defs></svg>

<div class="abs prod" style="left:89px"><div class="img" role="img" aria-label="Koi food tub" style="background:linear-gradient(#e26a2c,#3e63a8)"></div>
<div class="stars"><svg viewBox="0 0 24 24" fill="#f7a441"><use href="#star"/></svg><svg viewBox="0 0 24 24" fill="#f7a441"><use href="#star"/></svg><svg viewBox="0 0 24 24" fill="#f7a441"><use href="#star"/></svg><svg viewBox="0 0 24 24" fill="#ddd"><use href="#star"/></svg><svg viewBox="0 0 24 24" fill="#ddd"><use href="#star"/></svg></div>
<div class="pname">Koivita Mini<br>Granulate</div><div class="price">€8.99<small>250 ml</small></div><svg class="cart" viewBox="0 0 24 24"><path d="M2 3h4l3 11h11l3-8H7z"/><circle cx="10" cy="19" r="2"/><circle cx="18" cy="19" r="2"/></svg></div>

<div class="abs prod" style="left:287px"><div class="img" role="img" aria-label="Poultry grain bag" style="background:linear-gradient(#2f9a86,#b9a98c)"></div>
<div class="stars"><svg viewBox="0 0 24 24" fill="#f7a441"><use href="#star"/></svg><svg viewBox="0 0 24 24" fill="#f7a441"><use href="#star"/></svg><svg viewBox="0 0 24 24" fill="#f7a441"><use href="#star"/></svg><svg viewBox="0 0 24 24" fill="#f7a441"><use href="#star"/></svg><svg viewBox="0 0 24 24" fill="#ddd"><use href="#star"/></svg></div>
<div class="pname">Koivita Mini<br>Granulate</div><div class="price">€8.99<small>250 ml</small></div><svg class="cart" viewBox="0 0 24 24"><path d="M2 3h4l3 11h11l3-8H7z"/><circle cx="10" cy="19" r="2"/><circle cx="18" cy="19" r="2"/></svg></div>

<div class="abs prod" style="left:485px"><div class="img" role="img" aria-label="Pink fish food pouch" style="background:linear-gradient(#c9386f,#e9e9e9)"></div>
<div class="stars"><svg viewBox="0 0 24 24" fill="#f7a441"><use href="#star"/></svg><svg viewBox="0 0 24 24" fill="#f7a441"><use href="#star"/></svg><svg viewBox="0 0 24 24" fill="#f7a441"><use href="#star"/></svg><svg viewBox="0 0 24 24" fill="#f7a441"><use href="#star"/></svg><svg viewBox="0 0 24 24" fill="#ddd"><use href="#star"/></svg></div>
<div class="pname">Koivita Mini<br>Granulate</div><div class="price">€8.99<small>250 ml</small></div><svg class="cart" viewBox="0 0 24 24"><path d="M2 3h4l3 11h11l3-8H7z"/><circle cx="10" cy="19" r="2"/><circle cx="18" cy="19" r="2"/></svg></div>

<div class="abs prod" style="left:683px"><div class="img" role="img" aria-label="Chick crumb feed bag" style="left:45px;width:96px;background:linear-gradient(90deg,#eee,#e8d25a)"></div>
<div class="stars"><svg viewBox="0 0 24 24" fill="#f7a441"><use href="#star"/></svg><svg viewBox="0 0 24 24" fill="#f7a441"><use href="#star"/></svg><svg viewBox="0 0 24 24" fill="#f7a441"><use href="#star"/></svg><svg viewBox="0 0 24 24" fill="#f7a441"><use href="#star"/></svg><svg viewBox="0 0 24 24" fill="#ddd"><use href="#star"/></svg></div>
<div class="pname">Koivita Mini<br>Granulate</div><div class="price">€8.99<small>250 ml</small></div><svg class="cart" viewBox="0 0 24 24"><path d="M2 3h4l3 11h11l3-8H7z"/><circle cx="10" cy="19" r="2"/><circle cx="18" cy="19" r="2"/></svg></div>

<div class="abs prod" style="left:882px"><div class="img" role="img" aria-label="Yellow feed bucket" style="left:50px;width:86px;background:linear-gradient(#f2c21b,#c9a36b)"></div>
<div class="stars"><svg viewBox="0 0 24 24" fill="#f7a441"><use href="#star"/></svg><svg viewBox="0 0 24 24" fill="#f7a441"><use href="#star"/></svg><svg viewBox="0 0 24 24" fill="#f7a441"><use href="#star"/></svg><svg viewBox="0 0 24 24" fill="#ddd"><use href="#star"/></svg><svg viewBox="0 0 24 24" fill="#ddd"><use href="#star"/></svg></div>
<div class="pname">Koivita Mini<br>Granulate</div><div class="price">€8.99<small>250 ml</small></div><svg class="cart" viewBox="0 0 24 24"><path d="M2 3h4l3 11h11l3-8H7z"/><circle cx="10" cy="19" r="2"/><circle cx="18" cy="19" r="2"/></svg></div>

<div class="abs" style="left:1089px;top:1403px;width:39px;height:39px;border-radius:50%;background:var(--dark)"><svg viewBox="0 0 24 24" width="39" height="39" fill="none" stroke="#fff" stroke-width="2"><path d="M11 8l4 4-4 4"/></svg></div>

<h2 class="abs" style="left:87px;top:1636px">Special Offers / Promotions</h2>
<section class="abs" style="left:89px;top:1692px;width:1019px;height:294px;border-radius:44px;background:linear-gradient(90deg,#fff3e3,#fde0bb 60%,#fbc681)"></section>
<div class="abs" role="img" aria-label="Premium fish feed bags with koi carp" style="left:548px;top:1762px;width:430px;height:266px;border-radius:18px;background:radial-gradient(ellipse at 45% 50%,#5b4a8c 0%,#8d7fb2 38%,rgba(255,255,255,0) 72%)"></div>
<h2 class="abs" style="left:195px;top:1768px;font-size:26px">This Week's Deals</h2>
<p class="abs lead" style="left:195px;top:1812px">Enjoy discounts on selected fish and poultry<br>feed. Don't miss out on limited-time offers!</p>
<div class="abs btn" style="left:196px;top:1869px;width:203px;height:45px">VIEW ALL OFFERS <b><svg viewBox="0 0 24 24" fill="none" stroke="#f7a441" stroke-width="3"><path d="M5 12h13M13 6l6 6-6 6"/></svg></b></div>

<div class="abs usp" style="left:197px;top:2124px"><div class="c" style="background:var(--dark)"><svg viewBox="0 0 24 24"><path d="M1 6h13v10H1zM14 9h4l4 4v3h-8z"/><circle cx="5" cy="18" r="2"/><circle cx="18" cy="18" r="2"/></svg></div><div><h4>Free Shipping</h4><p>On all orders above<br>€50</p></div></div>
<div class="abs usp" style="left:479px;top:2124px"><div class="c" style="background:var(--orange)"><svg viewBox="0 0 24 24"><path d="M1 6h13v10H1zM14 9h4l4 4v3h-8z"/><circle cx="5" cy="18" r="2"/><circle cx="18" cy="18" r="2"/></svg></div><div><h4>Fast Delivery</h4><p>Nationwide delivery<br>within 2–3 days</p></div></div>
<div class="abs usp" style="left:763px;top:2124px"><div class="c" style="background:var(--dark)"><svg viewBox="0 0 24 24"><circle cx="12" cy="9" r="7"/><path d="M7 14l-3 8 4-2 2 3 2-5 2 5 2-3 4 2-3-8z"/></svg></div><div><h4>Quality Guaranteed</h4><p>Premium feed selected<br>by experts</p></div></div>

<h2 class="abs" style="left:88px;top:2318px">Why Choose Brenvik.nl?</h2>
<ul class="abs list">
  <li><svg viewBox="0 0 24 24"><circle cx="12" cy="12" r="11" fill="#3c3c3b"/><path d="M7 12l3 3 7-7" stroke="#fff" stroke-width="3" fill="none"/></svg>Over 25 years of experience in animal nutrition</li>
  <li><svg viewBox="0 0 24 24"><circle cx="12" cy="12" r="11" fill="#3c3c3b"/><path d="M7 12l3 3 7-7" stroke="#fff" stroke-width="3" fill="none"/></svg>Trusted by farms, breeders, and hobbyists</li>
  <li><svg viewBox="0 0 24 24"><circle cx="12" cy="12" r="11" fill="#3c3c3b"/><path d="M7 12l3 3 7-7" stroke="#fff" stroke-width="3" fill="none"/></svg>Carefully selected, premium-quality ingredients</li>
  <li><svg viewBox="0 0 24 24"><circle cx="12" cy="12" r="11" fill="#3c3c3b"/><path d="M7 12l3 3 7-7" stroke="#fff" stroke-width="3" fill="none"/></svg>Fast and reliable nationwide delivery</li>
  <li><svg viewBox="0 0 24 24"><circle cx="12" cy="12" r="11" fill="#3c3c3b"/><path d="M7 12l3 3 7-7" stroke="#fff" stroke-width="3" fill="none"/></svg>Excellent customer support</li>
</ul>
<div class="abs btn" style="left:88px;top:2587px;width:174px;height:46px;padding-left:36px">LEARN MORE <b><svg viewBox="0 0 24 24" fill="none" stroke="#f7a441" stroke-width="3"><path d="M5 12h13M13 6l6 6-6 6"/></svg></b></div>
<div class="abs" role="img" aria-label="Brown and white hens in a barn" style="left:502px;top:2324px;width:297px;height:316px;border-radius:24px;background:linear-gradient(160deg,#c9b8a5,#8a4a2a 60%,#6b4a38)"></div>
<div class="abs" role="img" aria-label="Tropical fish over a coral reef" style="left:813px;top:2324px;width:295px;height:316px;border-radius:24px;background:linear-gradient(180deg,#4aa6c9,#1e6f95 60%,#7a73a8)"></div>

<section class="abs about"></section>
<div class="abs" role="img" aria-label="Farmer feeding hens in a yard" style="left:650px;top:2800px;width:400px;height:400px;border-radius:50%;background:radial-gradient(circle at 55% 45%,#a85a4a,#7a5a48 50%,#5a4a40)"></div>
<h2 class="abs" style="left:95px;top:2858px;color:var(--white);font-size:26px">About Brenvik.nl</h2>
<div class="abs about-copy">
  <p>Lorem ipsum dolor sit amet, consectetur adipiscing elit. Donec tincidunt, ipsum a tincidunt ullamcorper, purus justo porta sapien, sed euismod enim nisl vel arcu. Vivamus vehicula, magna at mattis varius, mi turpis luctus massa, eget viverra leo augue nec justo. Sed suscipit, orci sed congue eleifend, justo lectus tincidunt mi, at sollicitudin lectus mi id nibh.</p>
  <p style="margin-top:18px">Lorem ipsum dolor sit amet, consectetur adipiscing elit. Donec tincidunt, ipsum a tincidunt ullamcorper, purus justo porta sapien</p>
</div>

<div class="abs brand" style="left:91px;top:3325px;font-size:62px;gap:10px"><i style="width:56px;height:56px"></i>brenvik</div>
<div class="abs fcol" style="left:393px;top:3305px"><h5>Customer Service</h5><a>Shipping &amp; Delivery</a><a>Returns &amp; Refunds</a><a>Payment Options</a><a>Contact Us</a></div>
<div class="abs fcol" style="left:619px;top:3305px"><h5>About Brenvik.nl</h5><a>Our Story</a><a>Sustainability</a><a>Careers</a><a>Blog</a></div>
<div class="abs fcol" style="left:811px;top:3305px"><h5>My Account</h5><a>Login / Register</a><a>Order History</a><a>Wishlist</a></div>
<div class="abs fcol" style="left:956px;top:3305px"><h5>Stay Connected</h5>
  <div class="ci"><svg viewBox="0 0 24 24"><path d="M12 1a8 8 0 018 8c0 6-8 14-8 14S4 15 4 9a8 8 0 018-8z"/></svg><a>Brenvik B.V., Amsterdam,<br>The Netherlands</a></div>
  <div class="ci"><svg viewBox="0 0 24 24"><path d="M2 5h20v14H2z"/></svg><a>info@brenvik.nl</a></div>
  <div class="ci"><svg viewBox="0 0 24 24"><path d="M6 2l4 5-2 3c1 3 3 5 6 6l3-2 5 4-3 4C10 21 3 14 2 5z"/></svg><a>+31 20 555 0192</a></div>
</div>
<div class="abs" style="left:91px;top:3516px;width:1020px;height:1px;background:var(--line)"></div>
<div class="abs social" style="left:119px;top:3533px"></div>
<div class="abs social" style="left:168px;top:3533px"></div>
<div class="abs social" style="left:213px;top:3533px"></div>
<div class="abs" style="left:496px;top:3547px;font-size:11px">© 2025 Brenvik.nl — All Rights Reserved</div>
<div class="abs" style="left:903px;top:3547px;font-size:11px">Terms &amp; Conditions | Privacy Policy</div>
<div class="abs" style="left:1134px;top:3496px;width:40px;height:40px;border-radius:50%;background:var(--orange)"><svg viewBox="0 0 24 24" width="40" height="40" fill="none" stroke="#fff" stroke-width="2"><path d="M8 14l4-4 4 4"/></svg></div>

</body>
</html>
```